Pregnancy and Fertility Information Website

Hello Designers,
I need a website which provide tips and information about healthy and happy pregnancy. My website name is Lorvin medical.

The website should provide all the information needed throughout pregnancy and beyond ranging from pregnancy tracking tools and articles about common pregnancy concerns and what to expect during pregnancy,etc.
The details about first trimester, second trimester and third trimester should be highlighted in the website.

Top Navigation
Home, Fertility, Pregnancy basics, Articles, Tips and News

I'm looking for a simple and clean design which involves captivating images and colors but it shouldn't be crowded. The design must be professional and modern. An easy to navigate layout is a must.

Green, violet, blue and light yellow colors are my favorites but i'm open to other options.

Any questions. Kindly ask

Industry/Entity Type

Medical

```html
<!DOCTYPE html>
<html lang="en">
<head>
<meta charset="utf-8">
<title>Lorvin medical – Pregnancy &amp; Fertility</title>
<link href="https://fonts.googleapis.com/css2?family=Dosis:wght@400;500;600;700;800&family=Noto+Serif:wght@400;700&display=swap" rel="stylesheet">
<style>
:root{
  --stage:#4a3b38;
  --green:#a6bf2b;
  --green-dark:#8ea51e;
  --purple:#8b3d8c;
  --purple-soft:#b27cb3;
  --pink:#d64fbf;
  --lilac:#f6eaf4;
  --cream:#fdfde3;
  --brown:#5a4532;
  --ink:#2a2a2a;
  --grey:#8a8a8a;
  --dark:#2b2521;
  --orange:#f0641e;
  --white:#ffffff;
}
*{box-sizing:border-box;margin:0;padding:0}
html,body{width:1200px;height:3000px;overflow:hidden}
body{background:var(--stage);font-family:"Noto Serif",Georgia,serif;color:var(--ink);position:relative}
.site{position:absolute;left:45px;top:60px;width:1110px;height:2296px;background:var(--white);overflow:hidden}
.abs{position:absolute}

/* header */
.header{position:absolute;left:0;top:0;width:1110px;height:56px;background:var(--white);z-index:2}
.header .phone{left:254px;top:6px;font-family:"Dosis",sans-serif;font-size:10px;color:var(--grey);display:flex;align-items:center;gap:6px}
.header .address{right:256px;top:6px;font-family:"Dosis",sans-serif;font-size:10px;color:var(--grey)}
.icon-dot{width:14px;height:14px;border-radius:50%;background:var(--green);display:inline-flex;align-items:center;justify-content:center}
.brand{left:0;width:1110px;top:4px;text-align:center;font-family:"Dosis",sans-serif;font-weight:700;font-size:12px;color:var(--green-dark)}
.brand .mark{display:block;width:26px;height:26px;border-radius:50%;background:var(--orange);margin:3px auto 0}
.nav a{position:absolute;top:32px;font-family:"Dosis",sans-serif;font-weight:600;font-size:10px;text-transform:uppercase;color:var(--ink);text-decoration:none;letter-spacing:.3px;white-space:nowrap}
.nav a.active{color:var(--green-dark)}

/* hero */
.hero{position:absolute;left:0;top:56px;width:1110px;height:490px}
.hero-photo{position:absolute;inset:0;background:linear-gradient(90deg,#e6f0d6 0%,#eef4e4 35%,#f3e5d8 60%,#e8c9ae 80%,#f2f3ea 100%)}
.hero-curve{position:absolute;left:0;bottom:0}
.hero-title{left:184px;top:122px;font-family:"Dosis",sans-serif;font-weight:600;font-size:40px;line-height:44px;color:var(--brown);text-align:center;width:290px}
.hero-tag{left:150px;top:238px;width:360px;text-align:center;font-family:"Dosis",sans-serif;font-weight:600;font-size:17px;color:#7b6a4a}
.hero-brand{left:150px;top:268px;width:360px;text-align:center;font-family:"Dosis",sans-serif;font-weight:800;font-size:22px;letter-spacing:1px;color:var(--green-dark);text-transform:uppercase}
.hero-mark{left:296px;top:306px;width:68px;height:68px;border-radius:50%;background:var(--orange)}

/* section titles */
.sec-title{position:absolute;left:0;width:1110px;text-align:center;font-family:"Dosis",sans-serif;font-weight:700;font-size:24px;color:var(--green-dark);text-transform:uppercase}
.sec-sub{position:absolute;left:0;width:1110px;text-align:center;font-size:9px;color:#666}
.sec-rule{position:absolute;left:531px;width:48px;height:2px;background:var(--green)}

/* stages */
.stages{position:absolute;left:0;top:546px;width:1110px;height:550px}
.stages-backdrop{left:0;top:110px;width:1110px;height:300px;background:linear-gradient(180deg,rgba(246,234,244,0) 0%,#f7eef6 40%,#f4e6f2 100%)}
.stage-item{position:absolute;left:196px;width:264px;text-align:right}
.stage-item h3{font-family:"Dosis",sans-serif;font-weight:700;font-size:11px;color:var(--ink);text-transform:uppercase}
.stage-item p{font-size:8px;line-height:11px;color:var(--grey);margin-top:4px;padding-left:40px}
.stage-badge{position:absolute;left:478px;width:38px;height:38px;border-radius:50%;background:var(--purple-soft);border:3px solid #e6cfe6}
.ribbon{left:664px;top:164px;width:140px;height:22px;background:var(--pink);color:#fff;font-family:"Dosis",sans-serif;font-weight:700;font-size:10px;text-align:center;line-height:22px;text-transform:uppercase}
.figures{left:586px;top:200px;width:268px;height:210px;background:linear-gradient(180deg,#9b4b9c,#7d3480);border-radius:120px 120px 6px 6px;opacity:.9}
.stage-bar{left:584px;top:416px;width:272px;height:18px;display:flex;gap:2px}
.stage-bar span{flex:1;background:var(--purple);color:#fff;font-size:9px;text-align:center;line-height:18px;font-family:"Noto Serif",serif;white-space:nowrap}
.stage-bar span:last-child{background:var(--pink)}
.faint-band{left:90px;top:476px;width:1024px;height:44px;background:#f7ecf5;display:flex;justify-content:space-around;align-items:center;font-size:22px;color:#eed7ea;font-family:"Noto Serif",serif}

/* guide */
.guide{position:absolute;left:0;top:1096px;width:1110px;height:424px;background:var(--cream)}
.guide-ring{left:0;top:0}
.guide-center{left:466px;top:190px;width:180px;height:180px;border-radius:50%;overflow:hidden;border:5px solid #fff;background:linear-gradient(180deg,#e9ddd2 0%,#d8c3b6 50%,#b6a2c2 100%)}
.guide-center .label{position:absolute;left:0;bottom:0;width:100%;height:82px;background:rgba(139,61,140,.72);color:#fff;font-family:"Dosis",sans-serif;font-weight:700;font-size:20px;line-height:22px;text-align:center;padding-top:14px;text-transform:uppercase}
.g-icon{position:absolute;width:44px;height:44px;border-radius:50%;background:var(--green);border:4px solid #eef3c8;display:flex;align-items:center;justify-content:center}
.g-item{position:absolute;width:200px}
.g-item h3{font-family:"Dosis",sans-serif;font-weight:700;font-size:11px;text-transform:uppercase;color:var(--ink)}
.g-item p{font-size:8px;line-height:11px;color:var(--grey);margin-top:3px}
.g-left{text-align:right}

/* posts */
.posts{position:absolute;left:0;top:1520px;width:1110px;height:432px}
.card{position:absolute;top:128px;width:186px}
.card-img{width:186px;height:130px;border-radius:3px}
.card-date{position:absolute;left:6px;top:114px;width:32px;height:32px;border-radius:50%;background:var(--green);border:3px solid #fff;color:#fff;font-family:"Dosis",sans-serif;font-weight:700;font-size:7px;line-height:9px;text-align:center;padding-top:5px}
.card h3{margin-top:18px;font-family:"Dosis",sans-serif;font-weight:700;font-size:11px;line-height:14px;color:var(--ink);text-transform:uppercase}
.card p{margin-top:8px;font-size:8px;line-height:11px;color:var(--grey)}
.card .more{position:absolute;top:244px;left:0;width:70px;height:18px;border:1px solid #ddd;border-radius:9px;font-family:"Dosis",sans-serif;font-weight:700;font-size:7px;text-align:center;line-height:16px;color:var(--ink)}

/* footer */
.footer{position:absolute;left:0;top:1952px;width:1110px;height:208px;background:linear-gradient(90deg,#2a2420,#3a302a 50%,#2a2420)}
.f-col{position:absolute;top:52px}
.f-col h4{font-family:"Dosis",sans-serif;font-weight:700;font-size:10px;color:#fff;text-transform:uppercase}
.f-col ul{list-style:none;margin-top:12px}
.f-col li{font-size:8px;color:#bdb5ae;line-height:17px;display:flex;align-items:center;gap:6px}
.f-col.about li{line-height:22px}
.bullet{width:4px;height:4px;border-radius:50%;background:#bdb5ae}
.f-photo{left:714px;top:48px;width:110px;height:122px;background:linear-gradient(135deg,#e7b8b0,#c98a86 60%,#a76766)}
.subscribe{position:absolute;left:0;top:2160px;width:1110px;height:86px;background:var(--green)}
.subscribe h4{position:absolute;left:254px;top:30px;font-family:"Dosis",sans-serif;font-weight:700;font-size:12px;color:#fff;text-transform:uppercase}
.subscribe p{position:absolute;left:254px;top:46px;font-size:7px;color:#f4f8dd}
.sub-input{left:440px;top:32px;width:210px;height:22px;border:1px solid #e4eeb8;border-radius:11px;padding-left:12px;font-size:7px;line-height:20px;color:#e4eeb8}
.sub-send{position:absolute;right:6px;top:4px;width:12px;height:12px;border-radius:50%;background:#e4eeb8}
.social{position:absolute;top:32px;width:22px;height:22px;border:1px solid #eaf2c4;border-radius:50%}
.bottom-bar{position:absolute;left:0;top:2246px;width:1110px;height:50px;background:#1f1b18}
.bottom-bar p{position:absolute;left:254px;top:18px;font-size:8px;color:#8a817a}
.bottom-bar b{color:var(--green);font-weight:400}
</style>
</head>
<body>
<div class="site">

  <header class="header">
    <div class="abs phone"><span class="icon-dot"><svg width="8" height="8" viewBox="0 0 10 10"><path d="M2 1l2 2-1 1c.6 1.3 1.7 2.4 3 3l1-1 2 2-1.5 1.5C4.5 9 1 5.5 .5 2.5z" fill="#fff"/></svg></span>(02) 55-010-234</div>
    <div class="abs brand">LORVIN MEDICAL<span class="mark"></span></div>
    <div class="abs address">Address - 14 Alder Lane NSW 2000</div>
    <nav class="nav">
      <a class="active" style="left:254px">Home</a>
      <a style="left:306px">Fertility</a>
      <a style="left:376px">Pregnancy Basics</a>
      <a style="left:658px">Articles</a>
      <a style="left:722px">Tips &amp; News</a>
      <a style="left:804px">Contact Us</a>
    </nav>
  </header>

  <section class="hero">
    <div class="hero-photo" role="img" aria-label="Photo of a mother gently holding her sleeping newborn baby"></div>
    <svg class="hero-curve" width="1110" height="60" viewBox="0 0 1110 60" preserveAspectRatio="none"><path d="M0 30 Q555 70 1110 30 L1110 60 L0 60z" fill="#fff"/></svg>
    <h1 class="abs hero-title">Feel Safe With Mom’s Care</h1>
    <p class="abs hero-tag">Best resource needed throughout pregnancy</p>
    <p class="abs hero-brand">Lorvin medical</p>
    <span class="abs hero-mark"></span>
  </section>

  <section class="stages">
    <div class="abs stages-backdrop" role="img" aria-label="Faint row of pregnant woman silhouettes across the section"></div>
    <h2 class="sec-title" style="top:50px">Pregnancy Stages</h2>
    <p class="sec-sub" style="top:84px">This section provides information about Trimesters</p>
    <span class="sec-rule" style="top:102px"></span>

    <div class="stage-item" style="top:158px"><h3>I Trimester</h3><p>This gives information about the 1st trimester. Lorem ipsum dolor sit amet, consectetur adipiscing elit, sed do eiusmod tempor.</p></div>
    <span class="stage-badge" style="top:160px"></span>
    <div class="stage-item" style="top:242px"><h3>II Trimester</h3><p>This gives information about the 2nd trimester. Lorem ipsum has been the industry's standard dummy text ever since the 1500s.</p></div>
    <span class="stage-badge" style="top:244px"></span>
    <div class="stage-item" style="top:330px"><h3>III Trimester</h3><p>This gives information about the 3rd trimester. Lorem ipsum is simply dummy text of the printing and typesetting industry.</p></div>
    <span class="stage-badge" style="top:332px"></span>
    <div class="stage-item" style="top:414px"><h3>Birth</h3><p>This gives information about the pregnancy birth. Lorem ipsum dolor sit amet, consectetur adipiscing elit, sed do eiusmod tempor.</p></div>
    <span class="stage-badge" style="top:416px"></span>

    <div class="abs ribbon">Pregnancy Stages</div>
    <div class="abs figures" role="img" aria-label="Four purple silhouettes of a woman at each stage of pregnancy and after birth"></div>
    <div class="abs stage-bar"><span>I Trimester</span><span>II Trimester</span><span>III Trimester</span><span>Birth</span></div>
    <div class="abs faint-band"><span>I Trimester</span><span>II Trimester</span><span>III Trimester</span><span>Birth</span></div>
  </section>

  <section class="guide">
    <h2 class="sec-title" style="top:46px">Pregnancy Guide</h2>
    <p class="sec-sub" style="top:80px">This provides all the details related to the pregnancy</p>
    <span class="sec-rule" style="top:98px"></span>
    <svg class="abs guide-ring" width="1110" height="424"><circle cx="556" cy="280" r="130" fill="none" stroke="#f1f3cf" stroke-width="2"/><circle cx="556" cy="280" r="104" fill="#fbfbd4"/></svg>
    <div class="abs guide-center" role="img" aria-label="Photo of a pregnant woman reading a guide">
      <div class="label">Pregnancy<br>Guide</div>
    </div>

    <span class="g-icon" style="left:442px;top:166px"><svg width="14" height="14"><circle cx="7" cy="7" r="6" fill="#fff"/></svg></span>
    <div class="g-item g-left" style="left:226px;top:168px"><h3>Getting Pregnant</h3><p>Lorem Ipsum is simply dummy text of the printing and typesetting industry</p></div>
    <span class="g-icon" style="left:404px;top:258px"><svg width="14" height="14"><rect x="1" y="4" width="12" height="8" rx="2" fill="#fff"/></svg></span>
    <div class="g-item g-left" style="left:188px;top:258px"><h3>Your First Scan</h3><p>Lorem Ipsum is simply dummy text of the printing and typesetting industry</p></div>
    <span class="g-icon" style="left:442px;top:350px"><svg width="14" height="14"><circle cx="7" cy="7" r="6" fill="#fff"/></svg></span>
    <div class="g-item g-left" style="left:226px;top:352px"><h3>Pregnant</h3><p>Lorem Ipsum is simply dummy text of the printing and typesetting industry</p></div>

    <span class="g-icon" style="left:626px;top:166px"><svg width="14" height="14"><circle cx="7" cy="7" r="6" fill="#fff"/></svg></span>
    <div class="g-item" style="left:686px;top:168px"><h3>Baby Birth</h3><p>Lorem Ipsum is simply dummy text of the printing and typesetting industry</p></div>
    <span class="g-icon" style="left:664px;top:258px"><svg width="14" height="14"><rect x="4" y="1" width="6" height="12" rx="2" fill="#fff"/></svg></span>
    <div class="g-item" style="left:724px;top:258px"><h3>Feeding Baby</h3><p>Lorem Ipsum is simply dummy text of the printing and typesetting industry</p></div>
    <span class="g-icon" style="left:626px;top:350px"><svg width="14" height="14"><circle cx="7" cy="7" r="6" fill="#fff"/></svg></span>
    <div class="g-item" style="left:686px;top:352px"><h3>Baby Care</h3><p>Lorem Ipsum is simply dummy text of the printing and typesetting industry</p></div>
  </section>

  <section class="posts">
    <h2 class="sec-title" style="top:54px">Latest Posts</h2>
    <p class="sec-sub" style="top:88px">Latest articles published by Lorvin Medical</p>
    <span class="sec-rule" style="top:106px"></span>

    <article class="card" style="left:258px">
      <div class="card-img" role="img" aria-label="Photo of a baby's hand held by an adult" style="background:linear-gradient(135deg,#f1d9cf,#d59b8a 60%,#a4655a)"></div>
      <span class="card-date">FEB<br>12</span>
      <h3>10 Simple Baby Care Tricks Mom Never Told You</h3>
      <p>Your mom has been there through the ups and downs, the heartaches and the good times, but she doesn't know everything.</p>
      <span class="more">READ MORE</span>
    </article>
    <article class="card" style="left:464px">
      <div class="card-img" role="img" aria-label="Photo of parents with their newborn in a hospital room" style="background:linear-gradient(135deg,#e8e2d8,#c9b7a4 55%,#8f7868)"></div>
      <span class="card-date">FEB<br>12</span>
      <h3>Parents Say: How to Care for a Newborn Baby</h3>
      <p>The first few weeks with your newborn will be chaotic. Here are a few tips from experienced parents to help guide.</p>
      <span class="more">READ MORE</span>
    </article>
    <article class="card" style="left:668px">
      <div class="card-img" role="img" aria-label="Photo of a smiling newborn baby lying on a blanket" style="background:linear-gradient(135deg,#f4e2d6,#ddb3a0 55%,#b5806e)"></div>
      <span class="card-date">FEB<br>12</span>
      <h3>Parenting Care-Bonding With Your Newborn</h3>
      <p>When experts talk about bonding, they're referring to the intense attachment you develop with your baby.</p>
      <span class="more">READ MORE</span>
    </article>
  </section>

  <footer>
    <div class="footer">
      <div class="f-col about" style="left:254px"><h4>About Lorvin Medical</h4>
        <ul><li><span class="bullet"></span>Contact Us</li><li><span class="bullet"></span>(02) 55-010-234</li><li><span class="bullet"></span>www.lorvinmedical.com</li><li><span class="bullet"></span>14 Alder Lane NSW 2000</li></ul></div>
      <div class="f-col" style="left:424px"><h4>Navigation</h4>
        <ul><li><span class="bullet"></span>Fertility</li><li><span class="bullet"></span>Pregnancy Basics</li><li><span class="bullet"></span>Articles</li><li><span class="bullet"></span>Tips &amp; News</li><li><span class="bullet"></span>Contact Us</li></ul></div>
      <div class="f-col" style="left:562px"><h4>Extra Navigation</h4>
        <ul><li><span class="bullet"></span>Getting Pregnant</li><li><span class="bullet"></span>Your First Scan</li><li><span class="bullet"></span>Pregnant</li><li><span class="bullet"></span>Baby Birth</li><li><span class="bullet"></span>Feeding Baby</li></ul></div>
      <div class="abs f-photo" role="img" aria-label="Photo of a newborn's feet cupped in a parent's hands"></div>
    </div>
    <div class="subscribe">
      <h4>Subscribe to us!</h4>
      <p>Subscribe to our monthly newsletter</p>
      <div class="abs sub-input">Enter your email<span class="sub-send"></span></div>
      <span class="social" style="left:700px"></span>
      <span class="social" style="left:731px"></span>
      <span class="social" style="left:762px"></span>
      <span class="social" style="left:793px"></span>
      <span class="social" style="left:824px"></span>
    </div>
    <div class="bottom-bar"><p>© Copyright <b>Lorvin Medical</b> 2015. All rights reserved.</p></div>
  </footer>

</div>
</body>
</html>
```